Medical Simulation - Creative Graphic for Data

My company needs a creative graph that depicts the rationales (or reasons) our learners chose certain drug options. Basically, our clients not only want to know how many times certain drugs were selected, but the "whys" behind their choices. I would like a PPT graphic that I can use for other deliverables, where I can simply switch out the drug (treatment) names, the "whys" (what we call rationales), and the specific metrics (percentages, "n" numbers, etc), and the graphic will update and adjust to the new information. The title of the graph (or the slide where the graph will live) should be something like "Treatment Rationales" or something to that effect. Include a placeholder for text to go if anyone wants to add an analysis of the graphic later. This placeholder should accommodate 2-3 bullet points of text. We want this graphic to not just be an image, but organized in a way that you would see in a presentation slide, with a title, place holder for analysis (as indicated above), branding colors, and helpful information to understand the graphic (what is included in this post and it's associated attachments).

I've included specific drug names, rationales, and metrics to use for this (please see excel document). If you are going to design the graph directly in PPT, please use the PPT template design included. Please don't feel like you have to use 1 slide only or can have multiple graphs, if that makes sense for you design idea. They just need to fit within the coloring of the PPT. For font, please use Arial. Below is a Google Drive Link to branding colors and vector art.

https://files.plorvex.net/open?id=7QkR2mTw8-LpXa04vNbHcY3TnpRd

We are open to many variations and design ideas. Please don't feel like you have to limit yourself! I've attached a few ideas that we've had and it may be a good place to start. We would ESPECIALLY like to see a version utilizing the radial graph (similar to the one included in the Rationales_DesignIdeas document).

Please reach out if you have any questions. Thanks!

Industry/Entity Type

Drug

Requirements
Nice to have
• It would be great to see the radial graph as a design variation (see link below)
• http://4.vistragrid.net/products/vistragrid/docs/users-guide/img/Samples/radar-chart-fixed-radius.png

```html
<!DOCTYPE html>
<html lang="en">
<head>
<meta charset="utf-8">
<title>Treatment Rationales</title>
<link rel="stylesheet" href="https://fonts.googleapis.com/css2?family=Arimo:wght@400;700&display=swap">
<style>
:root{
  --navy:#0e3a5b;
  --navy-deep:#0b2f4b;
  --blue:#1f6e9c;
  --sky:#8cc8ea;
  --orange:#f7923a;
  --olive:#a3a84a;
  --charcoal:#55585b;
  --grey:#8a8d90;
  --ink:#3a3f44;
  --paper:#ffffff;
  --stage:#e6e7e8;
}
*{box-sizing:border-box;margin:0;padding:0}
html,body{width:1200px;height:690px;overflow:hidden;background:var(--stage);font-family:"Arimo",Arial,sans-serif;color:var(--ink)}
.deck{position:relative;width:1200px;height:690px}
.slide{position:absolute;width:587px;height:330px;background:var(--paper);overflow:hidden;box-shadow:0 1px 4px rgba(0,0,0,.25)}
.s1{left:8px;top:10px}
.s2{left:606px;top:10px}
.s3{left:8px;top:350px}
.s4{left:606px;top:350px}
.abs{position:absolute}
.brand{position:absolute;font-size:18px;font-weight:700;color:var(--navy);letter-spacing:-.3px;line-height:1}
svg{display:block}

/* cover */
.cover-photo{position:absolute;inset:0;background:linear-gradient(120deg,#e9e2d8 0%,#d9cdbd 45%,#cbb49a 70%,#a27854 100%)}
.cover-shape{position:absolute;inset:0}
.cover-kicker{left:48px;top:107px;font-size:14px;color:#fff;letter-spacing:.2px}
.cover-kicker b{font-weight:400;color:var(--orange)}
.cover-title{left:48px;top:126px;font-size:24px;font-weight:700;color:#fff;letter-spacing:.5px}
.cover-date{left:48px;top:167px;font-size:21px;color:var(--olive)}
.cover-by{left:50px;top:195px;font-size:11.5px;color:#fff}
.url-pill{left:48px;top:214px;width:200px;height:19px;border-radius:10px;background:#fff;display:flex;align-items:center;overflow:hidden}
.url-pill .globe{width:34px;height:19px;background:#c9cbcd;display:flex;align-items:center;justify-content:center}
.url-pill span{flex:1;text-align:center;font-size:9px;color:var(--ink);padding-right:10px}

/* shared titles */
.kicker{font-size:15px;color:var(--orange);line-height:1}
.headline{font-size:22px;font-weight:700;color:var(--navy);line-height:1;letter-spacing:.3px}
.pageno{position:absolute;left:8px;bottom:8px;width:20px;height:20px;border-radius:50%;background:var(--navy-deep);color:#fff;font-size:7px;display:flex;align-items:center;justify-content:center}
.pageline{position:absolute;left:32px;bottom:17px;height:0;border-top:1px dotted #9aa3aa}

/* slide 2 table */
.tbl-head{left:32px;top:83px;width:230px;height:26px;background:var(--navy);color:#fff;font-size:7px;line-height:1.1;display:flex;align-items:center}
.tbl-head .c1{width:56px;padding-left:6px}
.tbl-row{position:absolute;left:6px;width:250px;height:24px;display:flex;align-items:center;font-size:6.5px;color:#6b7075;border-bottom:1px dotted #c7ccd0}
.tbl-row .num{width:24px;height:24px;color:#fff;display:flex;align-items:center;justify-content:center;font-size:7px}
.tbl-row .n{width:46px;padding-left:10px}
.tbl-row .t{flex:1;line-height:1.15;padding-left:8px}
.rat-head{font-size:14px;font-weight:700;color:var(--navy);border-bottom:2px solid var(--orange);padding-bottom:3px;width:124px}
.rat-item{position:absolute;left:460px;font-size:7px;color:var(--ink)}

/* slide 3 */
.s3 .kicker,.s3 .headline{text-align:right}
.rat-sub{left:404px;top:108px;font-size:19px;color:var(--ink);border-bottom:2px solid var(--orange);padding-bottom:2px;width:128px}
.bullets{left:412px;top:140px;list-style:none;font-size:8px;color:var(--ink);line-height:10px}
.bullets li::before{content:"";display:inline-block;border-left:4px solid var(--blue);border-top:2.5px solid transparent;border-bottom:2.5px solid transparent;margin-right:6px}
.legend-title{left:48px;top:236px;font-size:17px;color:var(--ink)}
.key{position:absolute;font-size:6.5px;color:var(--ink);display:flex;align-items:center}
.key::before{content:"";width:12px;height:0;border-top:1.5px solid var(--c);margin-right:2px}
.key i{width:4px;height:4px;border-radius:50%;background:var(--c);margin:0 3px 0 -9px}
.axis-label{position:absolute;font-size:6.5px;color:#6b7075;text-align:center}

/* slide 4 */
.dark-band{position:absolute;left:0;top:0;width:587px;height:221px;background:var(--navy)}
.s4 .kicker{color:#fff}
.s4 .headline{color:var(--orange)}
.leg-head{left:482px;top:72px;font-size:13px;font-weight:700;color:#fff;border-bottom:2px solid var(--orange);padding-bottom:3px;width:96px}
.lkey{position:absolute;left:484px;font-size:6.5px;color:#fff;display:flex;align-items:flex-start;line-height:1.2}
.lkey::before{content:"";width:12px;border-top:1px solid var(--c);margin:4px 4px 0 0;flex:none}
.tag{left:29px;top:226px;width:124px;height:19px;background:var(--olive);color:#fff;font-size:11px;font-weight:700;padding-left:6px;display:flex;align-items:center}
.trow{position:absolute;font-size:6.5px;color:#6b7075;display:flex;align-items:center}
.trow .dot{width:5px;height:5px;border-radius:50%;border:1px solid var(--c);margin-right:10px}
.trow b{width:42px;color:var(--ink);font-weight:700}
</style>
</head>
<body>
<main class="deck">

  <!-- Cover -->
  <section class="slide s1">
    <div class="cover-photo" role="img" aria-label="Softly blurred room interior with a white chair by a bright window and a wooden floor"></div>
    <svg class="cover-shape" width="587" height="330" viewBox="0 0 587 330">
      <polygon points="0,0 308,0 446,200 346,330 0,330" fill="var(--navy)"/>
      <polyline points="308,0 446,200 346,330" fill="none" stroke="rgba(255,255,255,.55)" stroke-width="3"/>
      <polyline points="326,0 466,200 366,330" fill="none" stroke="rgba(255,255,255,.25)" stroke-width="14"/>
    </svg>
    <p class="abs cover-kicker"><b>TREATMENT</b> RATIONALES</p>
    <h1 class="abs cover-title">PRESENTATION</h1>
    <p class="abs cover-date">Oct 2016</p>
    <p class="abs cover-by">Presented by : Jane Roe</p>
    <div class="abs url-pill">
      <div class="globe"><svg width="12" height="12" viewBox="0 0 12 12"><circle cx="6" cy="6" r="5" fill="none" stroke="#fff"/><ellipse cx="6" cy="6" rx="2.2" ry="5" fill="none" stroke="#fff"/><line x1="1" y1="6" x2="11" y2="6" stroke="#fff"/></svg></div>
      <span>www.medlyne.org</span>
    </div>
    <span class="brand" style="left:496px;top:12px">Medlyne</span>
  </section>

  <!-- Radial rings -->
  <section class="slide s2">
    <div class="abs" style="left:14px;top:16px"><p class="kicker">TREATMENT</p><h2 class="headline">RATIONALES</h2></div>

    <div class="abs tbl-head"><span class="c1"># OF DRUG<br>SELECTIONS</span><span>TREATMENT</span></div>
    <div class="tbl-row" style="top:109px"><span class="num" style="background:var(--blue)">01</span><span class="n">n = 20</span><span class="t">Irinotecan</span></div>
    <div class="tbl-row" style="top:133px"><span class="num" style="background:var(--sky)">02</span><span class="n">n = 100</span><span class="t">Irinotecan / leucovorin / 5-FU<br>plus bevacizumab</span></div>
    <div class="tbl-row" style="top:157px"><span class="num" style="background:var(--orange)">03</span><span class="n">n = 30</span><span class="t">Irinotecan / leucovorin / 5-FU<br>plus cetuximab</span></div>
    <div class="tbl-row" style="top:181px"><span class="num" style="background:var(--olive)">04</span><span class="n">n = 70</span><span class="t">Oxaliplatin / capecitabine</span></div>
    <div class="tbl-row" style="top:205px"><span class="num" style="background:var(--charcoal)">05</span><span class="n">n = 50</span><span class="t">Oxaliplatin / capecitabine<br>plus bevacizumab</span></div>
    <div class="tbl-row" style="top:229px"><span class="num" style="background:var(--navy)">06</span><span class="n">n = 30</span><span class="t">Oxaliplatin / leucovorin / 5-FU</span></div>
    <div class="tbl-row" style="top:253px"><span class="num" style="background:var(--navy-deep)">07</span><span class="n">n = 50</span><span class="t">Oxaliplatin / leucovorin / 5-FU<br>plus bevacizumab</span></div>

    <svg class="abs" style="left:0;top:0" width="587" height="330" viewBox="0 0 587 330" font-family="Arimo,Arial,sans-serif">
      <circle cx="314" cy="172" r="122" fill="#fff"/>
      <g transform="rotate(-90 314 172)" fill="none">
        <!-- ring 04 -->
        <g stroke-width="26">
          <circle cx="314" cy="172" r="107" pathLength="100" stroke="var(--blue)" stroke-dasharray="15 100"/>
          <circle cx="314" cy="172" r="107" pathLength="100" stroke="var(--sky)" stroke-dasharray="15 100" stroke-dashoffset="-15"/>
          <circle cx="314" cy="172" r="107" pathLength="100" stroke="var(--olive)" stroke-dasharray="8 100" stroke-dashoffset="-30"/>
          <circle cx="314" cy="172" r="107" pathLength="100" stroke="var(--charcoal)" stroke-dasharray="22 100" stroke-dashoffset="-38"/>
          <circle cx="314" cy="172" r="107" pathLength="100" stroke="var(--navy)" stroke-dasharray="40 100" stroke-dashoffset="-60"/>
        </g>
        <!-- ring 03 -->
        <g stroke-width="22">
          <circle cx="314" cy="172" r="82" pathLength="100" stroke="var(--sky)" stroke-dasharray="12 100"/>
          <circle cx="314" cy="172" r="82" pathLength="100" stroke="var(--olive)" stroke-dasharray="10 100" stroke-dashoffset="-12"/>
          <circle cx="314" cy="172" r="82" pathLength="100" stroke="var(--charcoal)" stroke-dasharray="20 100" stroke-dashoffset="-22"/>
          <circle cx="314" cy="172" r="82" pathLength="100" stroke="var(--sky)" stroke-dasharray="10 100" stroke-dashoffset="-42"/>
          <circle cx="314" cy="172" r="82" pathLength="100" stroke="var(--navy)" stroke-dasharray="48 100" stroke-dashoffset="-52"/>
        </g>
        <!-- ring 02 -->
        <g stroke-width="22">
          <circle cx="314" cy="172" r="59" pathLength="100" stroke="var(--blue)" stroke-dasharray="32 100"/>
          <circle cx="314" cy="172" r="59" pathLength="100" stroke="var(--sky)" stroke-dasharray="20 100" stroke-dashoffset="-32"/>
          <circle cx="314" cy="172" r="59" pathLength="100" stroke="var(--orange)" stroke-dasharray="24 100" stroke-dashoffset="-52"/>
          <circle cx="314" cy="172" r="59" pathLength="100" stroke="var(--olive)" stroke-dasharray="16 100" stroke-dashoffset="-76"/>
          <circle cx="314" cy="172" r="59" pathLength="100" stroke="var(--charcoal)" stroke-dasharray="8 100" stroke-dashoffset="-92"/>
        </g>
        <!-- ring 01 -->
        <g stroke-width="22">
          <circle cx="314" cy="172" r="36" pathLength="100" stroke="var(--sky)" stroke-dasharray="12 100"/>
          <circle cx="314" cy="172" r="36" pathLength="100" stroke="var(--orange)" stroke-dasharray="36 100" stroke-dashoffset="-12"/>
          <circle cx="314" cy="172" r="36" pathLength="100" stroke="var(--olive)" stroke-dasharray="32 100" stroke-dashoffset="-48"/>
          <circle cx="314" cy="172" r="36" pathLength="100" stroke="var(--charcoal)" stroke-dasharray="8 100" stroke-dashoffset="-80"/>
          <circle cx="314" cy="172" r="36" pathLength="100" stroke="var(--navy)" stroke-dasharray="12 100" stroke-dashoffset="-88"/>
        </g>
      </g>
      <g fill="none" stroke="#fff" stroke-width="1">
        <circle cx="314" cy="172" r="25"/><circle cx="314" cy="172" r="47"/><circle cx="314" cy="172" r="70"/><circle cx="314" cy="172" r="93"/><circle cx="314" cy="172" r="120"/>
      </g>
      <line x1="314" y1="52" x2="314" y2="147" stroke="#fff" stroke-width="1.5"/>
      <g font-size="5.5" fill="#fff" text-anchor="middle">
        <text x="338" y="150">16%</text><text x="342" y="188">50%</text><text x="298" y="200">50%</text><text x="288" y="160">19%</text>
        <text x="362" y="146">50%</text><text x="348" y="225">36%</text><text x="272" y="148">17%</text><text x="268" y="205">50%</text>
        <text x="350" y="104">18%</text><text x="390" y="150">17%</text><text x="382" y="210">42%</text><text x="246" y="182">50%</text><text x="266" y="115">26%</text>
        <text x="392" y="100">50%</text><text x="418" y="216">27%</text><text x="222" y="178">50%</text><text x="264" y="90">38%</text><text x="336" y="274">42%</text>
      </g>
      <g font-size="7" text-anchor="middle" fill="var(--navy)" font-weight="700">
        <circle cx="314" cy="76" r="8" fill="#fff"/><text x="314" y="78.5">04</text>
        <circle cx="314" cy="99" r="8" fill="#fff"/><text x="314" y="101.5">03</text>
        <circle cx="314" cy="122" r="8" fill="#fff"/><text x="314" y="124.5">02</text>
        <circle cx="314" cy="145" r="8" fill="#fff"/><text x="314" y="147.5">01</text>
      </g>
      <g stroke="#6b7075" stroke-width=".6" stroke-dasharray="1.5 1.5">
        <line x1="322" y1="76" x2="453" y2="76"/><line x1="322" y1="99" x2="453" y2="99"/>
        <line x1="322" y1="122" x2="453" y2="122"/><line x1="322" y1="145" x2="453" y2="145"/>
      </g>
      <g fill="var(--navy)">
        <polygon points="453,74 457,76 453,78"/><polygon points="453,97 457,99 453,101"/>
        <polygon points="453,120 457,122 453,124"/><polygon points="453,143 457,145 453,147"/>
      </g>
    </svg>
    <div class="abs rat-head" style="left:444px;top:44px">RATIONALES:</div>
    <p class="rat-item" style="top:72px">Recent guidelines</p>
    <p class="rat-item" style="top:95px">Preserves future treatment options</p>
    <p class="rat-item" style="top:118px">Impact on quality of life</p>
    <p class="rat-item" style="top:141px">Fewer overall side effects</p>

    <div class="pageno">2</div>
    <div class="pageline" style="width:470px"></div>
    <span class="brand" style="left:502px;top:304px">Medlyne</span>
  </section>

  <!-- Radar -->
  <section class="slide s3">
    <div class="abs" style="right:34px;top:18px"><p class="kicker">TREATMENT</p><h2 class="headline">RATIONALES</h2></div>
    <p class="axis-label" style="left:140px;top:23px;width:100px">Fewer overall side effects</p>
    <p class="axis-label" style="left:290px;top:126px;width:90px;text-align:left">Impact on quality of life</p>
    <p class="axis-label" style="left:150px;top:230px;width:80px">Preserves future treatment options</p>
    <p class="axis-label" style="left:26px;top:126px;width:70px;text-align:right">Recent guidelines</p>
    <svg class="abs" style="left:0;top:0" width="400" height="240" viewBox="0 0 400 240">
      <defs>
        <polygon id="oct" points="0,-96 67.9,-67.9 96,0 67.9,67.9 0,96 -67.9,67.9 -96,0 -67.9,-67.9"/>
      </defs>
      <g transform="translate(190 130)" fill="none">
        <g stroke="#d7dadd" stroke-width=".7">
          <use href="#oct" transform="scale(.1)" vector-effect="non-scaling-stroke"/>
          <use href="#oct" transform="scale(.2)" vector-effect="non-scaling-stroke"/>
          <use href="#oct" transform="scale(.3)" vector-effect="non-scaling-stroke"/>
          <use href="#oct" transform="scale(.4)" vector-effect="non-scaling-stroke"/>
          <use href="#oct" transform="scale(.5)" vector-effect="non-scaling-stroke"/>
          <use href="#oct" transform="scale(.6)" vector-effect="non-scaling-stroke"/>
          <use href="#oct" transform="scale(.7)" vector-effect="non-scaling-stroke"/>
          <use href="#oct" transform="scale(.8)" vector-effect="non-scaling-stroke"/>
          <use href="#oct" transform="scale(.9)" vector-effect="non-scaling-stroke"/>
          <use href="#oct"/>
          <path d="M0,-96V96M-96,0H96M-67.9,-67.9L67.9,67.9M67.9,-67.9L-67.9,67.9"/>
        </g>
        <g stroke-width="1.4" stroke-linejoin="round">
          <polygon stroke="var(--grey)" points="0,-38.4 20.4,-20.4 28.8,0 13.6,13.6 0,38.4 -20.4,20.4 -72,0 -3.4,-3.4"/>
          <polygon stroke="var(--sky)" points="0,-96 67.9,-67.9 28.8,0 6.8,6.8 0,9.6 -13.6,13.6 -33.6,0 -1.4,-1.4"/>
          <polygon stroke="var(--olive)" points="0,-38.4 23.8,-23.8 67.2,0 40.7,40.7 0,9.6 -10.2,10.2 -52.8,0 -1.4,-1.4"/>
          <polygon stroke="var(--orange)" points="0,-4.8 67.9,-67.9 96,0 67.9,67.9 0,4.8 -1.4,1.4 -1.9,0 -1.4,-1.4"/>
          <polygon stroke="var(--charcoal)" points="0,-28.8 3.4,-3.4 4.8,0 3.4,3.4 0,96 -61.1,61.1 -96,0 -1.4,-1.4"/>
          <polygon stroke="var(--blue)" points="0,-1.9 3.4,-3.4 4.8,0 3.4,3.4 0,96 -40.7,40.7 -81.6,0 -1.4,-1.4"/>
          <polygon stroke="var(--navy)" points="0,-9.6 6.8,-6.8 4.8,0 6.8,6.8 0,19.2 -6.8,6.8 -9.6,0 -3.4,-3.4"/>
        </g>
        <g>
          <circle cx="0" cy="-96" r="2" fill="var(--sky)"/><circle cx="67.9" cy="-67.9" r="2" fill="var(--sky)"/>
          <circle cx="96" cy="0" r="2" fill="var(--orange)"/><circle cx="67.9" cy="67.9" r="2" fill="var(--orange)"/>
          <circle cx="0" cy="96" r="2" fill="var(--navy)"/><circle cx="-61.1" cy="61.1" r="2" fill="var(--charcoal)"/>
          <circle cx="-96" cy="0" r="2" fill="var(--charcoal)"/><circle cx="-81.6" cy="0" r="2" fill="var(--navy)"/>
          <circle cx="67.2" cy="0" r="2" fill="var(--olive)"/><circle cx="40.7" cy="40.7" r="2" fill="var(--olive)"/>
          <circle cx="-40.7" cy="40.7" r="2" fill="var(--navy)"/><circle cx="-72" cy="0" r="2" fill="var(--grey)"/>
          <circle cx="-52.8" cy="0" r="2" fill="var(--olive)"/><circle cx="0" cy="-38.4" r="2" fill="var(--grey)"/>
          <circle cx="20.4" cy="-20.4" r="2" fill="var(--grey)"/><circle cx="0" cy="-9.6" r="2" fill="var(--navy)"/>
        </g>
      </g>
    </svg>
    <h3 class="abs rat-sub">RATIONALES:</h3>
    <ul class="abs bullets">
      <li>Recent guidelines</li>
      <li>Preserves future treatment options</li>
      <li>Impact on quality of life</li>
      <li>Fewer overall side effects</li>
    </ul>
    <h3 class="abs legend-title">TREATMENT</h3>
    <p class="key" style="left:54px;top:263px;--c:var(--navy)"><i></i>irinotecan</p>
    <p class="key" style="left:54px;top:275px;--c:var(--orange)"><i></i>irinotecan/leucovorin/5-FU plus cetuximab</p>
    <p class="key" style="left:54px;top:287px;--c:var(--blue)"><i></i>oxaliplatin/capecitabine plus bevacizumab</p>
    <p class="key" style="left:54px;top:299px;--c:var(--grey)"><i></i>oxaliplatin/leucovorin/5-FU plus bevacizumab</p>
    <p class="key" style="left:216px;top:263px;--c:var(--olive)"><i></i>irinotecan/leucovorin/5-FU plus bevacizumab</p>
    <p class="key" style="left:216px;top:275px;--c:var(--sky)"><i></i>oxaliplatin/capecitabine</p>
    <p class="key" style="left:216px;top:287px;--c:var(--charcoal)"><i></i>oxaliplatin/leucovorin/5-FU</p>
    <div class="pageno" style="background:var(--navy-deep)">3</div>
    <div class="pageline" style="width:470px"></div>
    <span class="brand" style="left:502px;top:304px">Medlyne</span>
  </section>

  <!-- Line chart -->
  <section class="slide s4">
    <div class="dark-band"></div>
    <div class="abs" style="left:34px;top:18px"><p class="kicker">TREATMENT</p><h2 class="headline">RATIONALES</h2></div>
    <svg class="abs" style="left:0;top:0" width="480" height="221" viewBox="0 0 480 221" font-family="Arimo,Arial,sans-serif">
      <g stroke="#fff" stroke-width=".8">
        <line x1="41" y1="69" x2="41" y2="194"/><line x1="41" y1="194" x2="473" y2="194"/>
        <line x1="95" y1="69" x2="95" y2="194"/><line x1="149" y1="69" x2="149" y2="194"/><line x1="203" y1="69" x2="203" y2="194"/>
        <line x1="257" y1="69" x2="257" y2="194"/><line x1="311" y1="69" x2="311" y2="194"/><line x1="365" y1="69" x2="365" y2="194"/>
        <line x1="419" y1="69" x2="419" y2="194"/>
      </g>
      <g font-size="6.5" fill="#fff" text-anchor="end">
        <text x="36" y="72">60%</text><text x="36" y="93">50%</text><text x="36" y="114">40%</text><text x="36" y="135">30%</text>
        <text x="36" y="155">20%</text><text x="36" y="176">10%</text><text x="36" y="197">0%</text>
      </g>
      <g font-size="6.5" fill="#fff" text-anchor="middle">
        <text x="41" y="205">0</text><text x="95" y="205">1</text><text x="149" y="205">2</text><text x="203" y="205">3</text>
        <text x="257" y="205">4</text><text x="311" y="205">5</text><text x="365" y="205">6</text><text x="419" y="205">7</text><text x="473" y="205">8</text>
      </g>
      <g fill="none" stroke-width="1.2" stroke-linejoin="round">
        <path stroke="#7fb2d9" d="M95,90 C120,110 130,155 149,156.6 C175,158 190,90 203,90 C225,90 235,158 257,158.6 C280,158 295,112 311,106.6 C335,98 350,90 365,90 C390,92 410,110 419,115"/>
        <path stroke="var(--orange)" d="M95,90 C120,110 130,155 149,156.6 C175,158 190,90 203,90 C225,90 235,158 257,158.6 C280,158 295,112 311,106.6 C335,98 350,90 365,90 C395,90 410,125 419,139.9"/>
        <path stroke="#9fc89e" d="M95,90 C115,100 135,138 149,137.8 C175,136 190,92 203,90 C225,88 240,85 257,90 C280,100 295,175 311,177.4 C330,180 350,95 365,90 C395,90 410,145 419,158.6"/>
        <path stroke="var(--olive)" d="M95,90 C115,100 135,119 149,119.1 C170,119 185,92 203,90 C225,88 240,150 257,158.6 C275,168 295,177 311,177.4 C330,178 350,95 365,90 C395,90 410,145 419,158.6"/>
      </g>
      <g fill="var(--navy)" stroke-width=".9">
        <circle cx="95" cy="90" r="2" stroke="#fff"/><circle cx="149" cy="156.6" r="2" stroke="var(--orange)"/>
        <circle cx="149" cy="137.8" r="2" stroke="#7fb2d9"/><circle cx="149" cy="119.1" r="2" stroke="var(--olive)"/>
        <circle cx="203" cy="90" r="2" stroke="#fff"/><circle cx="257" cy="90" r="2" stroke="#fff"/>
        <circle cx="257" cy="158.6" r="2" stroke="#7fb2d9"/><circle cx="311" cy="106.6" r="2" stroke="#7fb2d9"/>
        <circle cx="311" cy="177.4" r="2" stroke="var(--olive)"/><circle cx="365" cy="90" r="2" stroke="#fff"/>
        <circle cx="419" cy="115" r="2" stroke="#7fb2d9"/><circle cx="419" cy="139.9" r="2" stroke="var(--orange)"/>
        <circle cx="419" cy="158.6" r="2" stroke="var(--olive)"/>
      </g>
      <g font-size="6.5" font-weight="700" fill="#fff" text-anchor="middle">
        <text x="95" y="84">50%</text><text x="149" y="114">36%</text><text x="149" y="132">27%</text><text x="149" y="152">18%</text>
        <text x="203" y="84">50%</text><text x="257" y="84">50%</text><text x="257" y="154">17%</text><text x="311" y="101">42%</text>
        <text x="311" y="172">8%</text><text x="365" y="84">50%</text><text x="419" y="109">38%</text><text x="419" y="134">26%</text>
        <text x="419" y="150">19%</text><text x="419" y="156">17%</text>
      </g>
    </svg>
    <div class="abs leg-head">RATIONALES:</div>
    <p class="lkey" style="top:98px;--c:#9fc89e">Fewer overall side effects</p>
    <p class="lkey" style="top:123px;--c:var(--olive)">Impact on quality of life</p>
    <p class="lkey" style="top:148px;--c:var(--orange)">Preserves future<br>treatment options</p>
    <p class="lkey" style="top:174px;--c:#7fb2d9">Recent guidelines</p>

    <div class="abs tag">TREATMENT:</div>
    <p class="trow" style="left:36px;top:256px;--c:var(--blue)"><span class="dot"></span><b>n = 20</b>Irinotecan</p>
    <p class="trow" style="left:36px;top:270px;--c:var(--sky)"><span class="dot"></span><b>n = 100</b>Irinotecan / leucovorin / 5-FU plus bevacizumab</p>
    <p class="trow" style="left:36px;top:284px;--c:var(--orange)"><span class="dot"></span><b>n = 30</b>Irinotecan / leucovorin / 5-FU plus cetuximab</p>
    <p class="trow" style="left:36px;top:298px;--c:var(--olive)"><span class="dot"></span><b>n = 70</b>Oxaliplatin / capecitabine</p>
    <p class="trow" style="left:276px;top:256px;--c:var(--charcoal)"><span class="dot"></span><b>n = 50</b>Oxaliplatin / capecitabine plus bevacizumab</p>
    <p class="trow" style="left:276px;top:270px;--c:var(--blue)"><span class="dot"></span><b>n = 30</b>Oxaliplatin / leucovorin / 5-FU</p>
    <p class="trow" style="left:276px;top:284px;--c:var(--navy)"><span class="dot"></span><b>n = 50</b>Oxaliplatin / leucovorin / 5-FU plus bevacizumab</p>

    <div class="pageno">4</div>
    <div class="pageline" style="width:470px"></div>
    <span class="brand" style="left:502px;top:304px">Medlyne</span>
  </section>

</main>
</body>
</html>
```